Sportswear for local soccer teams Ad

Looking for a banner ad to be placed in a local soccer associations website. Brawlinmoor Logo must be shown. It should be short, eyecatching and want teams to visit or contact us about their kits or training apparel. Brawlinmoor is a doric word for delighted so any play on happiness, delight is fine. Size allowable is : 605x80. Also looking for a Skyscraper to be placed on all subsequent pages on their site. Size : 240x900

Target Market(s)

Football Teams

Industry/Entity Type

Sports Bar

```html
<!DOCTYPE html>
<html lang="en">
<head>
<meta charset="utf-8">
<title>Brawlinmoor Skyscraper Ad 240x900</title>
<link rel="stylesheet" href="https://fonts.googleapis.com/css2?family=Oswald:wght@400;500;600;700&display=swap">
<style>
  :root {
    --page-bg: #eeeeee;
    --panel-top: #0b2530;
    --panel-mid: #123845;
    --panel-bottom: #0c2a35;
    --white: #ffffff;
    --accent-blue: #2fb8ec;
    --photo-green-light: #c8f08a;
    --photo-green: #7fc24a;
    --photo-dark: #2b2f33;
    --button-top: #f2f2f2;
    --button-bottom: #a9a9a9;
    --button-text: #1c2a30;
  }
  * { margin: 0; padding: 0; box-sizing: border-box; }
  html, body {
    width: 1200px;
    height: 2356px;
    overflow: hidden;
    background: var(--page-bg);
  }
  .skyscraper {
    position: absolute;
    left: 315px;
    top: 22px;
    width: 558px;
    height: 2106px;
    overflow: hidden;
    background: linear-gradient(180deg, var(--panel-top) 0%, var(--panel-mid) 55%, var(--panel-bottom) 100%);
    font-family: "Oswald", "Arial Narrow", sans-serif;
    color: var(--white);
    text-align: center;
    text-transform: uppercase;
  }
  .brand {
    position: absolute;
    top: 22px;
    left: 0;
    width: 100%;
  }
  .brand-mark {
    display: block;
    width: 92px;
    height: 92px;
    margin: 0 auto;
    border-radius: 50%;
    border: 6px solid var(--white);
  }
  .brand-name {
    display: block;
    margin-top: 10px;
    font-size: 44px;
    font-weight: 500;
    line-height: 1;
    letter-spacing: 1px;
  }
  .product-photo {
    position: absolute;
    top: 290px;
    left: 0;
    width: 558px;
    height: 850px;
  }
  .headline {
    position: absolute;
    left: 0;
    width: 100%;
    font-weight: 700;
    line-height: 1;
  }
  .headline-lead { top: 1226px; font-size: 76px; }
  .headline-main { top: 1312px; font-size: 158px; letter-spacing: 1px; }
  .tagline {
    position: absolute;
    top: 1516px;
    left: 0;
    width: 100%;
    font-size: 46px;
    font-weight: 600;
    line-height: 1;
    color: var(--accent-blue);
  }
  .offer {
    position: absolute;
    top: 1574px;
    left: 0;
    width: 100%;
    font-size: 40px;
    font-weight: 500;
    line-height: 58px;
  }
  .shop-button {
    position: absolute;
    top: 1798px;
    left: 101px;
    width: 305px;
    height: 88px;
    display: flex;
    align-items: center;
    justify-content: center;
    gap: 14px;
    background: linear-gradient(180deg, var(--button-top) 0%, var(--button-bottom) 100%);
    border-radius: 3px;
    color: var(--button-text);
    font-size: 40px;
    font-weight: 600;
    text-decoration: none;
  }
  .shop-button svg { width: 56px; height: 44px; }
  .site-url {
    position: absolute;
    top: 1982px;
    left: 0;
    width: 100%;
    font-size: 40px;
    font-weight: 500;
    line-height: 1;
  }
</style>
</head>
<body>
  <main class="skyscraper">
    <header class="brand">
      <span class="brand-mark"></span>
      <span class="brand-name">Brawlinmoor</span>
    </header>

    <svg class="product-photo" viewBox="0 0 558 850" role="img" aria-label="Product photo: pink and black shin guards, a grey and red soccer ball and black boots on a green sunburst background">
      <defs>
        <radialGradient id="photoGlow" cx="55%" cy="35%" r="75%">
          <stop offset="0%" stop-color="var(--photo-green-light)"/>
          <stop offset="55%" stop-color="var(--photo-green)"/>
          <stop offset="100%" stop-color="var(--photo-dark)"/>
        </radialGradient>
      </defs>
      <polygon points="0,30 558,0 558,790 0,850" fill="var(--white)"/>
      <polygon points="0,62 558,26 558,760 0,812" fill="url(#photoGlow)"/>
    </svg>

    <h1 class="headline headline-lead">Are you in a</h1>
    <p class="headline headline-main">Team?</p>
    <p class="tagline">We have you covered</p>
    <p class="offer">Check out our amazing<br>team deals</p>

    <a class="shop-button" href="#">
      Shop now
      <svg viewBox="0 0 28 22" aria-hidden="true">
        <path d="M1 2h4l3 12h14l3-9H7" fill="none" stroke="var(--button-text)" stroke-width="2" stroke-linejoin="round"/>
        <path d="M9 7h14M10 10h12" stroke="var(--button-text)" stroke-width="1.5"/>
        <circle cx="10" cy="18.5" r="2" fill="var(--button-text)"/>
        <circle cx="20" cy="18.5" r="2" fill="var(--button-text)"/>
      </svg>
    </a>

    <p class="site-url">www.brawlinmoor.com</p>
  </main>
</body>
</html>
```